Website design for a Cloud Computing solution company

Name Dorian
Title Head of marketing
Company Name 47Nimbo Solutions Co., Ltd.
E-mail address dorian.feng@47nimbo.example
Present URL (if any) www.47nimbo.example

Description of Project:

The web page style requirements: pages are clean, major color prefer light blue, white and black.
The current 4 Sketches as the page design reference.

What are the top three reasons why you currently have or want to build a Web site?

• Our products are mainly in the online sales.
• Easy to transfer our advantage and features of our product
• Built a communication platform based on cloud computing users to attract more users.

What are the target market that you would like to attract to your Web site and their demographics?

• Small and medium businesses .
• Personal webmaster.
• Startups Company via Internet.

What do you want a person to do once he or she comes to the site?
• Be interested in our product and click on child page to look up more information.
• Contacting with us on-line after browsing

LOOK AND FEEL: List example(s) of sites with a “look and feel” that you would like for your site.

https://www.lumavault.example

SITE ORGANIZATION & LAYOUT: List one or two examples of sites with navigation and layout similar to the one you would like to develop.

https://www.lumavault.example/

FEATURES: Please list all the features/facilities that you would like the website to provide your visitors. To help us understand better, please direct us to a sample site containing the feature.

1) We will use order pages templates and clinent management templates from SERVLEDGR.
2) All ICONs need to be redisigned and prefer to flat design.
3) Prefer to HTML5.
Is there any specific color scheme you want to follow or you like the most?

White and black overall and some light blue.

GRAPHICS: Do you have any graphics/logos/pictures that you would like us to use?

No.

If you have previously had a website, please indicate the features and ingredients that pleased you or displeased you.

No, we don't have existing website.

How can we look at that website?

www.tervanhost.example (Not existing website)

Do you have an existing logo?
No

Industry/Entity Type

Marketing

```html
<!DOCTYPE html>
<html lang="en">
<head>
<meta charset="utf-8">
<title>Tervan Cloud — Cloud Development</title>
<link rel="stylesheet" href="https://fonts.googleapis.com/css2?family=Open+Sans:wght@300;400;600;700&display=swap">
<style>
:root{
  --navy:#1f2f57;
  --blue:#1e6fd0;
  --blue-dark:#1457a8;
  --sky:#6fa8e8;
  --lavender:#e6e7f5;
  --violet:#7b7ed2;
  --violet-light:#9c9fe2;
  --slate:#4f5768;
  --slate-dark:#3e4554;
  --green:#3ab54a;
  --white:#ffffff;
  --ink:#222a38;
  --muted:#8a93a6;
}
*{box-sizing:border-box;margin:0;padding:0}
html,body{width:779px;height:1200px;overflow:hidden}
body{font-family:"Open Sans",Arial,sans-serif;color:var(--ink);background:var(--white);position:relative}
.abs{position:absolute}

/* header */
.site-header{left:0;top:0;width:779px;height:34px;background:var(--white);border-bottom:1px solid #d8dce6}
.brand{left:14px;top:7px;display:flex;align-items:center;gap:6px;font-size:15px;font-weight:600;color:var(--navy)}
.brand-dot{width:10px;height:10px;background:var(--blue);border-radius:50%}
.main-nav{left:162px;top:5px;display:flex;gap:4px;font-size:10px}
.main-nav a{color:var(--ink);text-decoration:none;padding:3px 10px;line-height:12px;text-align:center}
.main-nav a.active{background:var(--blue);color:var(--white);padding:5px 12px}
.login{left:620px;top:4px;width:156px}
.login-row{display:flex;gap:3px}
.login input{width:56px;height:12px;font-size:6px;border:1px solid #bfc5d2;padding:0 3px;font-family:inherit}
.login button{height:12px;font-size:6px;background:var(--blue);color:var(--white);border:0;padding:0 8px;font-family:inherit}
.login-note{font-size:7px;color:var(--muted);margin-top:3px}
.login-note span{color:var(--blue)}

/* hero */
.hero{left:0;top:34px;width:779px;height:330px;background:linear-gradient(180deg,#c9d7ea 0%,#8ea7c7 45%,#4d6d9a 100%)}
.hero-title{left:104px;top:135px;width:246px;height:100px;background:rgba(25,70,150,.75);color:var(--white);font-weight:700;font-size:24px;line-height:30px;text-align:center;padding-top:19px;border:1px solid rgba(255,255,255,.4)}
.features-box{left:454px;top:135px;width:234px;height:92px;background:rgba(30,90,180,.8);color:var(--white);padding:8px 10px;border:1px solid rgba(255,255,255,.4)}
.features-box h2{font-size:13px;font-weight:700;width:100px}
.features-box ul{position:absolute;left:122px;top:6px;list-style:none;font-size:11px;line-height:14px}
.features-box li::before{content:"";display:inline-block;width:7px;height:7px;background:var(--white);margin-right:4px}
.learn-more{left:10px;top:44px;background:var(--green);color:var(--white);font-size:10px;font-weight:600;padding:4px 9px;border-radius:2px}

/* action band */
.action-band{left:0;top:364px;width:779px;height:32px;background:linear-gradient(180deg,var(--blue),var(--blue-dark))}
.btn-band{top:5px;height:22px;background:linear-gradient(180deg,#5b95e0,#1b5fb4);color:var(--white);font-weight:700;font-size:13px;text-align:center;line-height:20px;border:1px solid #bcd4f2;border-radius:4px}

/* packages */
.packages{left:0;top:396px;width:779px;height:450px;background:var(--lavender)}
.section-title{width:779px;text-align:center;font-weight:300;font-size:30px;color:#3a3f55}
.plan{background:var(--white);box-shadow:0 2px 6px rgba(0,0,0,.25);text-align:center}
.plan-name{background:var(--navy);color:var(--white);font-weight:700;font-size:19px;height:40px;line-height:40px}
.plan-price{background:var(--blue);color:var(--white);font-size:14px;line-height:16px;padding:4px 0}
.plan ul{list-style:none;font-size:7px;color:#444}
.plan li{height:20px;line-height:20px;border-bottom:1px solid #e3e6ee}
.purchase{display:inline-block;margin-top:9px;background:var(--navy);color:var(--white);font-size:9px;font-weight:700;padding:4px 12px}

/* why us */
.why{left:0;top:846px;width:779px;height:250px;background:linear-gradient(180deg,var(--violet-light),var(--violet))}
.why-title{top:10px;color:var(--white);font-weight:700;font-size:17px;width:779px;text-align:center;letter-spacing:1px}
.why-title::before,.why-title::after{content:"";display:inline-block;width:26px;height:2px;background:var(--white);vertical-align:middle;margin:0 8px}
.benefit{width:180px;text-align:center;color:var(--white)}
.benefit svg{display:block;margin:0 auto}
.benefit h3{font-size:15px;font-weight:400;margin-top:3px;white-space:nowrap}
.benefit-note{width:120px;height:16px;margin:3px auto 0;background:#eef0fb;box-shadow:0 1px 3px rgba(0,0,0,.3)}

/* footer */
.site-footer{left:0;top:1096px;width:779px;height:104px;background:var(--slate);color:#d5d9e3}
.foot-col{top:10px;font-size:9px}
.foot-col h4{font-weight:400;font-size:9px;color:var(--white);margin-bottom:3px}
.foot-col p{font-size:6px;line-height:9px}
.social{left:558px;top:12px;display:flex;gap:5px}
.social span{width:13px;height:13px;border-radius:50%;background:#aeb5c4}
.tel{left:545px;top:42px;font-size:11px;color:var(--white)}
.copyright{left:0;top:88px;width:779px;height:16px;background:var(--slate-dark);font-size:6px;line-height:16px;text-align:center}
</style>
</head>
<body>

<header class="abs site-header">
  <div class="abs brand"><span class="brand-dot"></span>Tervan Cloud</div>
  <nav class="abs main-nav">
    <a class="active" href="#">Home</a><a href="#">Product</a><a href="#">Control</a><a href="#">Who's on<br>Tervan</a><a href="#">Help</a><a href="#">Company</a>
  </nav>
  <form class="abs login">
    <div class="login-row"><input placeholder="Email"><input placeholder="Password"><button type="button">Log In</button></div>
    <p class="login-note">Not a member yet? <span>Register now</span></p>
  </form>
</header>

<section class="abs hero" role="img" aria-label="Photo of a bright data centre aisle lined with server racks">
  <h1 class="abs hero-title">The Future of<br>Cloud Development</h1>
  <div class="abs features-box">
    <h2>Main Features</h2>
    <ul><li>lorem ipsum</li><li>lorem ipsum</li><li>lorem ipsum</li><li>lorem ipsum</li><li>lorem ipsum</li></ul>
    <span class="abs learn-more">Learn More</span>
  </div>
</section>

<div class="abs action-band">
  <a class="abs btn-band" style="left:109px;width:130px">Apply for Trial</a>
  <a class="abs btn-band" style="left:579px;width:92px">Contact Us</a>
</div>

<section class="abs packages">
  <h2 class="abs section-title" style="top:14px">Choose Any Package</h2>

  <div class="abs plan" style="left:104px;top:71px;width:182px;height:290px">
    <div class="plan-name">STANDARD</div>
    <div class="plan-price">$ 99 month<br>$ 399 year</div>
    <ul><li>2.4 GHZ</li><li>1 CPU+512 MEMORY</li><li>30 G SYSTEM DISK</li><li>50G DATA DISK</li><li>1 PUBLIC IP+1M BGP</li><li>MULTI OS TEMPLATES</li></ul>
    <span class="purchase">PURCHASE</span>
  </div>

  <div class="abs plan" style="left:306px;top:58px;width:195px;height:318px">
    <div class="plan-name">ADVANCE</div>
    <div class="plan-price">$ 199 month<br>$ 699 year</div>
    <ul><li>2.4 GHZ</li><li>2 CPU+2G MEMORY</li><li>30 G SYSTEM DISK</li><li>50G DATA DISK</li><li>1 PUBLIC IP+ 5M BGP</li><li>MULTI OS TEMPLATES</li></ul>
    <span class="purchase" style="margin-top:24px">PURCHASE</span>
  </div>

  <div class="abs plan" style="left:519px;top:71px;width:182px;height:290px">
    <div class="plan-name">LUXURIOUS</div>
    <div class="plan-price">$ 299 month<br>$ 999 year</div>
    <ul><li>2.4 GHZ</li><li>4 CPU+4G MEMORY</li><li>30 G SYSTEM DISK</li><li>100G DATA DISK</li><li>1 PUBLIC IP+10M BGP</li><li>MULTI OS TEMPLATES</li></ul>
    <span class="purchase">PURCHASE</span>
  </div>
</section>

<section class="abs why">
  <h2 class="abs why-title">Why Us</h2>

  <div class="abs benefit" style="left:80px;top:50px">
    <svg width="40" height="40" viewBox="0 0 40 40"><path d="M20 3 L34 9 V20 C34 29 27 35 20 37 C13 35 6 29 6 20 V9 Z" fill="#2a5fb8" stroke="#fff" stroke-width="2"/><path d="M20 6 V34" stroke="#fff" stroke-width="2"/></svg>
    <h3>Stringent Security</h3><div class="benefit-note"></div>
  </div>
  <div class="abs benefit" style="left:300px;top:50px">
    <svg width="40" height="40" viewBox="0 0 40 40"><circle cx="20" cy="20" r="18" fill="#2a5fb8"/><rect x="10" y="12" width="20" height="6" rx="1" fill="#fff"/><rect x="10" y="21" width="20" height="6" rx="1" fill="#fff"/><circle cx="27" cy="15" r="1.2" fill="#2a5fb8"/><circle cx="27" cy="24" r="1.2" fill="#2a5fb8"/></svg>
    <h3>Distributed Storage</h3><div class="benefit-note"></div>
  </div>
  <div class="abs benefit" style="left:510px;top:50px">
    <svg width="40" height="40" viewBox="0 0 40 40"><circle cx="20" cy="20" r="18" fill="#fff"/><path d="M5 21 H13 L16 13 L21 28 L25 17 L27 21 H35" fill="none" stroke="#2a5fb8" stroke-width="2.5"/></svg>
    <h3>Exceptional Reliability</h3><div class="benefit-note"></div>
  </div>

  <div class="abs benefit" style="left:80px;top:148px">
    <svg width="40" height="40" viewBox="0 0 40 40"><circle cx="20" cy="20" r="17" fill="#2a5fb8" stroke="#fff" stroke-width="2"/><ellipse cx="20" cy="20" rx="7" ry="17" fill="none" stroke="#fff" stroke-width="1.5"/><path d="M3 20 H37 M6 12 H34 M6 28 H34" stroke="#fff" stroke-width="1.5"/></svg>
    <h3>High Quality Network</h3><div class="benefit-note"></div>
  </div>
  <div class="abs benefit" style="left:300px;top:148px">
    <svg width="40" height="40" viewBox="0 0 40 40"><circle cx="20" cy="20" r="17" fill="#fff" stroke="#2a5fb8" stroke-width="3"/><path d="M20 9 V20 L28 24" fill="none" stroke="#2a5fb8" stroke-width="2.5"/></svg>
    <h3>Short Time To Setup</h3><div class="benefit-note"></div>
  </div>
  <div class="abs benefit" style="left:510px;top:148px">
    <svg width="40" height="40" viewBox="0 0 40 40"><rect x="5" y="7" width="30" height="20" rx="2" fill="#2a5fb8" stroke="#fff" stroke-width="2"/><path d="M15 33 H25 M20 27 V33" stroke="#fff" stroke-width="2.5"/></svg>
    <h3>7*24 Montioring</h3><div class="benefit-note"></div>
  </div>
</section>

<footer class="abs site-footer">
  <div class="abs foot-col" style="left:135px"><h4>Help</h4><p>FAQ<br>Guides<br>Status</p></div>
  <div class="abs foot-col" style="left:198px"><h4>Company</h4><p>About<br>News<br>Careers</p></div>
  <div class="abs foot-col" style="left:268px"><h4>Customers</h4><p>Stories<br>Partners</p></div>
  <div class="abs foot-col" style="left:335px"><h4>Support</h4><p>Tickets<br>Contact</p></div>
  <div class="abs social"><span></span><span></span><span></span><span></span></div>
  <p class="abs tel">Tel: 400-555-0100</p>
  <p class="abs copyright">© 2024 Tervan Cloud. All rights reserved.</p>
</footer>

</body>
</html>
```